Brindle Advisory Business Card Design

Business card for business consulting company, using attached logo. We do financial and strategic consulting, and want a clean, professional image with a bit of fun. Our logo is a flat whale tail, which symbolizes the Orca whale, a highly collaborative, group based animal that is very successful in navigating the ocean, protecting the herd, and hunting. We like the logo that is blue and gray on white one one side, but would be open to a blue card with white lettering on the other side... or whatever you'd suggest
Updates
Hi all - I have had the logo modified to take the shadowing off the tail. I will post it on the brief... under a file name called updated logo. thank you Added Saturday, April 25, 2015
Target Market(s)
Small to medium sized businesses ($10M to $500M in revenue per year), financial and sales executives, general managers, attorneys and CPAs
Industry/Entity Type
Financial
Contact Information for Business Card
Want company name, contact info - name, title, telephone, email, website, linkedin, twitter and Facebook. No physical address yet.
Requirements
Must have
- contemporary design, bold, strong, confident but with a bit of fun. prominently feature the logo and the whale tail icon
Nice to have
- unique touches that would differentiate us from a regular card... for example, logo and writing all on front on white background, but on back - logo in white on a blue background
- open to idea of different shapes of card than standard... but not sure
Should not have
- ?

```html
<!DOCTYPE html>
<html lang="en">
<head>
<meta charset="utf-8">
<title>Brindle Advisory Business Card</title>
<link href="https://fonts.googleapis.com/css2?family=Open+Sans:wght@400;600&display=swap" rel="stylesheet">
<style>
  :root {
    --backdrop: #e9e6e1;
    --blue-light: #2196dc;
    --blue-mid: #0f76c6;
    --blue-deep: #0a5aa8;
    --paper: #ffffff;
    --paper-shade: #eeeeee;
    --navy: #2a4a86;
    --slate: #56709c;
    --grey: #9a9a9a;
    --ink: #3c5a92;
  }
  * { margin: 0; padding: 0; box-sizing: border-box; }
  html, body {
    width: 1200px; height: 902px; overflow: hidden;
    background: var(--backdrop);
    font-family: "Open Sans", Arial, sans-serif;
  }
  .stage { position: relative; width: 1200px; height: 902px; }
  .card {
    position: absolute;
    width: 580px; height: 350px;
    border-radius: 26px;
    box-shadow: 0 10px 24px rgba(0,0,0,0.18);
  }
  .card--front {
    left: 80px; top: 80px;
    background: radial-gradient(ellipse at 45% 45%, var(--blue-light) 0%, var(--blue-mid) 55%, var(--blue-deep) 100%);
    display: flex; align-items: center; justify-content: center;
  }
  .card--back {
    left: 540px; top: 472px;
    background: radial-gradient(ellipse at 40% 40%, var(--paper) 0%, var(--paper) 50%, var(--paper-shade) 100%);
    padding: 40px 50px;
    display: flex; flex-direction: column; align-items: center;
  }
  .brand { display: flex; align-items: center; gap: 14px; }
  .brand__square { border-radius: 8px; flex: none; }
  .brand__text { display: flex; flex-direction: column; align-items: flex-end; }
  .brand__name { font-weight: 600; letter-spacing: -1px; line-height: 1; }
  .brand__tagline { font-weight: 400; line-height: 1; margin-top: 4px; }

  .card--front .brand__square { width: 74px; height: 74px; background: var(--paper); }
  .card--front .brand__name { font-size: 50px; color: var(--paper); }
  .card--front .brand__tagline { font-size: 15px; color: var(--paper); }

  .card--back .brand__square { width: 48px; height: 48px; background: var(--slate); border-radius: 6px; }
  .card--back .brand__name { font-size: 32px; color: var(--navy); }
  .card--back .brand__tagline { font-size: 11px; color: var(--grey); margin-top: 3px; }

  .person { margin-top: 26px; text-align: center; }
  .person__name { font-size: 26px; color: var(--navy); font-weight: 400; line-height: 1.1; }
  .person__title { font-size: 13px; color: var(--slate); margin-top: 2px; }

  .contact { margin-top: 22px; list-style: none; font-size: 14px; color: var(--ink); line-height: 1.45; }
  .contact__label { display: inline-block; min-width: 28px; }
</style>
</head>
<body>
<main class="stage">
  <section class="card card--front" aria-label="Card front">
    <div class="brand">
      <span class="brand__square"></span>
      <div class="brand__text">
        <span class="brand__name">Brindle Advisory</span>
        <span class="brand__tagline">business consulting</span>
      </div>
    </div>
  </section>

  <section class="card card--back" aria-label="Card back">
    <div class="brand">
      <span class="brand__square"></span>
      <div class="brand__text">
        <span class="brand__name">Brindle Advisory</span>
        <span class="brand__tagline">business consulting</span>
      </div>
    </div>
    <div class="person">
      <p class="person__name">Employee name</p>
      <p class="person__title">Managing Director</p>
    </div>
    <ul class="contact">
      <li><span class="contact__label">P :</span> 036-5190 2274</li>
      <li><span class="contact__label">IN :</span> brindleadvisory</li>
      <li><span class="contact__label">T :</span> @brindleadvisory</li>
      <li><span class="contact__label">E :</span> info@brindleadvisory.com</li>
      <li><span class="contact__label">W :</span> www.brindleadvisory.com</li>
      <li><span class="contact__label">F :</span> https://www.brindleadvisory.com/community</li>
    </ul>
  </section>
</main>
</body>
</html>
```